Simple, elegant, business card design required

Hi designers,I am looking for a simple yet elegant business card design.

Please make use of my logo (attached); you are free to tweak the logo should you wish to do so.

Our business is involved in many different fields - almost all of them involved in some form of "design", so that's really one of the key things I want to portray. I do not wish to specify which field of design, exactly.

I prefer white on black (or just monochromatic), but if you have a different, creative idea, I am open to that too.

You can use artsy photographs provided that you have the license to use those. Please feel free to ask me any questions.
Updates

Project Deadline Extended Reason: Small extension for potential revisions. Did not get the time to provide as much feedback as I can. Added Wednesday, July 09, 2014

Target Market(s)

High-end customers looking for design consultancy

Industry/Entity Type

Business

Contact Information for Business Card

Name: Gareth Moonfield
Position: Creative Director
Mobile: +155603928174
Address: Barrow Lane, Stratford upon Avon, Warwickshire GL12 4RT
Website: torvakest.com (not launched yet)

Requirements
Must have
• Design layout must be clean, original, and text must be readable when printed.
Should not have
• ~ No business card templates please. Anyone using this will be reported.
• ~ Please don't spam entries.

```html
<!DOCTYPE html>
<html lang="en">
<head>
<meta charset="utf-8">
<title>Torvakest – Business Card</title>
<link rel="stylesheet" href="https://fonts.googleapis.com/css2?family=Josefin+Sans:wght@300;400;600&family=Oswald:wght@500&display=swap">
<style>
  :root {
    --ink: #1c1c1c;
    --band-dark: #383838;
    --band-mid: #6b6b6b;
    --paper: #ffffff;
    --stage: #e7e5e1;
    --hatch: #d9d9d9;
    --muted: #3a3a3a;
  }
  * { margin: 0; padding: 0; box-sizing: border-box; }
  html, body { width: 1200px; height: 970px; overflow: hidden; background: var(--stage); }
  .stage { position: relative; width: 1200px; height: 970px; }

  .card {
    position: absolute; left: 240px; width: 720px; height: 411px;
    background: var(--paper); overflow: hidden;
    box-shadow: 0 10px 30px rgba(0,0,0,.18);
    font-family: "Josefin Sans", sans-serif; color: var(--ink);
  }
  .card--back { top: 50px; }
  .card--front { top: 509px; }

  .card__art { position: absolute; inset: 0; }

  .brand { position: absolute; display: flex; align-items: center; gap: 14px; }
  .brand__dot { border: 2px solid var(--ink); border-radius: 50%; }
  .brand__name { font-weight: 400; text-transform: uppercase; letter-spacing: .32em; }

  .card--back .brand { right: 70px; top: 62px; }
  .card--back .brand__dot { width: 22px; height: 22px; }
  .card--back .brand__name { font-size: 22px; }

  .card--front .brand { left: 150px; top: 92px; }
  .card--front .brand__dot { width: 34px; height: 34px; }
  .card--front .brand__name { font-size: 38px; }

  .person { position: absolute; right: 400px; top: 236px; text-align: right; }
  .person__name { font-family: "Oswald", sans-serif; font-weight: 500; font-size: 30px; letter-spacing: .02em; text-transform: uppercase; line-height: 1.05; }
  .person__role { font-size: 15px; letter-spacing: .14em; text-transform: uppercase; margin-top: 6px; }

  .divider { position: absolute; left: 340px; top: 226px; width: 2px; height: 96px; background: var(--ink); }

  .contacts { position: absolute; left: 360px; top: 226px; display: grid; grid-template-columns: auto auto; column-gap: 26px; row-gap: 10px; list-style: none; }
  .contact { display: flex; align-items: center; gap: 8px; font-size: 13px; color: var(--muted); white-space: nowrap; }
  .contact__icon { width: 20px; height: 20px; flex: none; }

  .front-bar { position: absolute; right: 0; bottom: 42px; width: 240px; height: 48px; }
  .edge-hatch { position: absolute; right: 0; top: 0; width: 26px; height: 100%; background: var(--hatch); }
</style>
</head>
<body>
<main class="stage">

  <section class="card card--back" aria-label="Card back">
    <svg class="card__art" viewBox="0 0 720 411" aria-hidden="true">
      <polygon points="0,150 470,150 300,250 0,250" fill="var(--band-dark)"/>
      <polygon points="0,250 300,250 215,300 0,300" fill="var(--band-mid)"/>
      <polygon points="590,0 720,0 720,18 560,18" fill="var(--ink)"/>
      <polygon points="470,150 720,0 720,16 490,150" fill="var(--ink)" opacity=".0"/>
    </svg>
    <div class="brand">
      <span class="brand__dot"></span>
      <span class="brand__name">Torvakest</span>
    </div>
  </section>

  <section class="card card--front" aria-label="Card front">
    <div class="edge-hatch" role="img" aria-label="Fine diagonal line texture along the right edge"></div>

    <div class="brand">
      <span class="brand__dot"></span>
      <span class="brand__name">Torvakest</span>
    </div>

    <div class="person">
      <p class="person__name">Gareth Moonfield</p>
      <p class="person__role">General Manager</p>
    </div>

    <span class="divider"></span>

    <ul class="contacts">
      <li class="contact">
        <svg class="contact__icon" viewBox="0 0 20 20" aria-hidden="true"><circle cx="10" cy="10" r="9" fill="none" stroke="var(--ink)" stroke-width="1.3"/><path d="M7 6c0 4 3 7 7 7l-1 -2-2 .5c-1-.6-2-1.6-2.5-2.5L9 7 7 6z" fill="var(--ink)"/></svg>
        +155603928174
      </li>
      <li class="contact">
        <svg class="contact__icon" viewBox="0 0 20 20" aria-hidden="true"><circle cx="10" cy="10" r="9" fill="none" stroke="var(--ink)" stroke-width="1.3"/><path d="M6 7h8v6H6z M6 7l4 3 4-3" fill="none" stroke="var(--ink)" stroke-width="1.2"/></svg>
        hello@torvakest.com
      </li>
      <li class="contact">
        <svg class="contact__icon" viewBox="0 0 20 20" aria-hidden="true"><circle cx="10" cy="10" r="9" fill="none" stroke="var(--ink)" stroke-width="1.3"/><rect x="7.5" y="5" width="5" height="10" rx="1" fill="none" stroke="var(--ink)" stroke-width="1.2"/></svg>
        +155603928174
      </li>
      <li class="contact">
        <svg class="contact__icon" viewBox="0 0 20 20" aria-hidden="true"><circle cx="10" cy="10" r="9" fill="none" stroke="var(--ink)" stroke-width="1.3"/><circle cx="10" cy="10" r="5" fill="none" stroke="var(--ink)" stroke-width="1"/><path d="M5 10h10M10 5c-2 3-2 7 0 10M10 5c2 3 2 7 0 10" fill="none" stroke="var(--ink)" stroke-width="1"/></svg>
        www.torvakest.com
      </li>
      <li class="contact">
        <svg class="contact__icon" viewBox="0 0 20 20" aria-hidden="true"><circle cx="10" cy="10" r="9" fill="none" stroke="var(--ink)" stroke-width="1.3"/><path d="M10 15c-3-3.5-4-5-4-6.5a4 4 0 0 1 8 0c0 1.5-1 3-4 6.5z" fill="var(--ink)"/><circle cx="10" cy="8.5" r="1.4" fill="var(--paper)"/></svg>
        Barrow Lane, GL12 4RT
      </li>
    </ul>

    <svg class="front-bar" viewBox="0 0 240 48" aria-hidden="true">
      <polygon points="24,0 240,0 240,48 0,48" fill="var(--ink)"/>
    </svg>
  </section>

</main>
</body>
</html>
```